Postcard Design

I need some postcards designed to be mailed by printharbor for my classic old world grille called the Copperleaf Grille in downtown Denver. We cater to executives and those looking for a classy meal out. I had some business cards designed by print harbor that I would like to use as a style guide for our postcards. The postcards are intended to advertise our Saturday Lobster Special. the headline needs to read "Lobster Saturdays" followed by "Half Priced French Fried Lobster served all night" as a subtitle. I would like the postcards to be black like my business cards if possible and include the same picture of the boxer my business card uses. I would like to use the same metallic gold font if possible as well. The postcards need to include:
Address: 2417 Alder Row (across from the historic Marlow Crest Hotel)
phone: 303-555-0147
Website: www.copperleafgrille-demo.com (maybe include "make a reservation online at www.copperleafgrille-demo.com"
Open from 5pm.
a map of where we are (maintaining a black background and using the font color (metallic gold as the streets... just so the map isn't copy pasted from google maps).

Attached are my business card (front and back) and a bigger version of the picture of the boxer I would like to incorporate.

```html
<!DOCTYPE html>
<html lang="en">
<head>
<meta charset="utf-8">
<title>Copperleaf Grille – Lobster Saturdays Postcard</title>
<link href="https://fonts.googleapis.com/css2?family=Oswald:wght@400;500;700&display=swap" rel="stylesheet">
<style>
  :root {
    --stage: #6f6f6f;
    --ink: #0d0d0d;
    --charcoal: #2b2b2b;
    --white: #ffffff;
    --gold: #b8974a;
    --gold-light: #d6bb72;
    --teal: #4f8c86;
    --paper: #fbfbfb;
    --line: #444444;
  }
  * { margin: 0; padding: 0; box-sizing: border-box; }
  html, body { width: 900px; height: 1200px; overflow: hidden; }
  body {
    background: var(--stage);
    font-family: 'Oswald', 'Arial Narrow', sans-serif;
    position: relative;
  }
  .postcard {
    position: absolute;
    left: 60px;
    width: 780px;
    overflow: hidden;
    box-shadow: 0 6px 18px rgba(0,0,0,.35);
  }

  /* Front */
  .postcard--front { top: 30px; height: 606px; background: var(--ink); }
  .front__photo {
    position: absolute; inset: 0;
    background: radial-gradient(ellipse at 55% 55%, #5a5a5a 0%, #2e2e2e 35%, #0e0e0e 75%);
  }
  .front__headline {
    position: absolute; left: 36px; top: 22px;
    color: var(--white); font-weight: 700; font-size: 40px;
    letter-spacing: 1px; text-transform: uppercase; line-height: 1;
  }
  .front__subtitle {
    position: absolute; left: 36px; top: 72px;
    color: var(--white); font-weight: 500; font-size: 30px;
    text-transform: uppercase; line-height: 1.15; letter-spacing: .5px;
  }
  .front__reserve {
    position: absolute; left: 36px; top: 178px;
    color: var(--white); font-weight: 400; font-size: 22px;
    text-transform: uppercase; letter-spacing: .5px;
  }
  .front__web {
    position: absolute; left: 36px; top: 210px;
    color: var(--teal); font-weight: 700; font-size: 36px; letter-spacing: .3px;
  }
  .brand {
    position: absolute; right: 40px; top: 36px;
    display: flex; align-items: center; gap: 10px;
    color: var(--white); font-weight: 700; font-size: 30px;
    text-transform: uppercase; letter-spacing: 1px;
  }
  .brand__dot { width: 14px; height: 14px; background: var(--white); }
  .open-band {
    position: absolute; left: 0; top: 390px;
    width: 330px; height: 138px;
    background: var(--teal);
    clip-path: polygon(0 0, 88% 0, 100% 100%, 0 100%);
  }
  .open-band__label {
    position: absolute; left: 36px; top: 416px;
    color: var(--white); font-weight: 400; font-size: 32px; line-height: 1.05;
  }
  .open-band__time {
    position: absolute; left: 132px; top: 400px;
    color: var(--white); font-weight: 700; font-size: 96px; line-height: 1;
  }
  .lobster-seal {
    position: absolute; left: 465px; top: 300px;
    width: 250px; height: 250px; border-radius: 50%;
    background: radial-gradient(circle at 40% 35%, var(--gold-light), var(--gold) 70%);
  }

  /* Back */
  .postcard--back { top: 654px; height: 522px; background: var(--paper); }
  .back__panel {
    position: absolute; left: 0; top: 0; bottom: 0; width: 450px;
    background: linear-gradient(135deg, #3a3a3a 0%, var(--charcoal) 60%, #1e1e1e 100%);
  }
  .back__brand {
    position: absolute; left: 0; width: 450px; top: 120px;
    display: flex; align-items: center; justify-content: center; gap: 12px;
    color: var(--ink); white-space: nowrap;
    font-weight: 700; font-size: 40px; line-height: 1;
    text-transform: uppercase; letter-spacing: 2px;
  }
  .back__brand-dot { width: 16px; height: 16px; background: var(--ink); flex: none; }
  .location {
    position: absolute; left: 60px; top: 330px; width: 330px; height: 96px;
    background: linear-gradient(90deg, var(--gold), var(--gold-light));
    border-radius: 48px 8px 8px 48px;
  }
  .location__map {
    position: absolute; left: 50px; top: 320px; width: 116px; height: 116px;
    border-radius: 50%; background: var(--white); border: 3px solid var(--gold);
  }
  .location__text {
    position: absolute; left: 180px; top: 338px;
    color: var(--white); font-size: 13px; line-height: 1.15;
  }
  .location__title { font-weight: 700; font-size: 16px; text-transform: uppercase; }
  .back__web {
    position: absolute; left: 0; width: 450px; bottom: 24px;
    text-align: center; color: var(--white); font-weight: 500; font-size: 20px;
  }
  .back__divider {
    position: absolute; left: 612px; top: 150px; width: 2px; height: 300px; background: #e2e2e2;
  }
  .stamp-box {
    position: absolute; right: 48px; top: 90px; width: 104px; height: 104px;
    border: 3px solid var(--line);
  }
</style>
</head>
<body>
  <section class="postcard postcard--front">
    <div class="front__photo" role="img" aria-label="Black and white photograph of a boxer in the ring"></div>
    <h1 class="front__headline">Lobster Saturdays</h1>
    <p class="front__subtitle">Half priced French fried<br>lobster served all night</p>
    <p class="front__reserve">Make a reservation online at</p>
    <p class="front__web">www.copperleafgrille-demo.com</p>
    <div class="brand"><span class="brand__dot"></span>Copperleaf Grille</div>
    <div class="open-band"></div>
    <p class="open-band__label">Open<br>from</p>
    <p class="open-band__time">5pm</p>
    <div class="lobster-seal" role="img" aria-label="Gold circle with a white lobster illustration"></div>
  </section>

  <section class="postcard postcard--back">
    <div class="back__panel"></div>
    <p class="back__brand"><span class="back__brand-dot"></span>Copperleaf Grille</p>
    <div class="location"></div>
    <div class="location__map" role="img" aria-label="Small street map showing the restaurant location"></div>
    <div class="location__text">
      <p class="location__title">Location</p>
      <p>2417 Alder Row</p>
      <p>Denver, CO 80202</p>
      <p>(Across from the</p>
      <p>Marlow Crest)</p>
    </div>
    <p class="back__web">www.copperleafgrille-demo.com</p>
    <div class="back__divider"></div>
    <div class="stamp-box"></div>
  </section>
</body>
</html>
```